QRV-TB 2018 Recycling Rate Report

We need a design for our 2018 Recycling Rate Report on Expanded Polystyrene. We want to move from a larger booklet style to a two page document. The report from last year - which was done as a booklet - is attached to provide an example of our style and design.The primary items that must be included (but not limited to) the information on pages 3, 5 & 7. The graphs must include room for 2018 data.To view our typical company design/style please see our website at www.qrvtradeboard.org. Our primary RGB colors are: (187,140,9); (94,47,29); (94,138,164); and (164,167,15). Secondary RGB colors are (249,162,28) and (218,210,208). Our title/header font is DIN Next LT Pro and our copy font is Calibri 10.5 pt. We can deviate from the font specification if beneficial and welcome interesting text treatments and typography.

Target Market(s)

Recycling facilities & general public.

Font styles to use
Sans Serif

Requirements
Must have
• Information presentation must be clean and easy to reference.

```html
<!DOCTYPE html>
<html lang="en">
<head>
<meta charset="utf-8">
<title>QRV-TB 2018 EPS Recycling Rate Report</title>
<link href="https://fonts.googleapis.com/css2?family=Raleway:wght@400;500;600;700&display=swap" rel="stylesheet">
<style>
:root{
  --brown:#5e2f1d;
  --gold:#bb8c09;
  --blue:#5e8aa4;
  --olive:#a4a70f;
  --orange:#f9a21c;
  --stone:#dad2d0;
  --white:#ffffff;
  --ink:#3a3a3a;
  --grid:#d9d9d9;
}
*{box-sizing:border-box;margin:0;padding:0}
html,body{width:1200px;height:450px;overflow:hidden;background:var(--brown)}
body{position:relative;font-family:"Raleway",sans-serif;color:var(--ink)}
.panel{position:absolute;border-radius:9px;overflow:hidden}
.panel--white{background:var(--white)}
.panel--blue{background:var(--blue);color:var(--white)}
.panel--olive{background:var(--olive);color:var(--white)}
.panel--orange{background:var(--orange)}
.heading{font-weight:500;font-size:13.5px;letter-spacing:.2px;line-height:16px}
.copy{font-size:6.6px;line-height:9.1px;text-align:justify}
.copy p+p{margin-top:9px}

/* cover */
.cover{left:11px;top:11px;width:129px;height:208px;text-align:right;padding:0 10px}
.brand{position:absolute;left:14px;top:22px;display:flex;align-items:center;gap:6px}
.brand-dot{width:34px;height:34px;border-radius:50%;background:var(--gold)}
.brand-name{font-size:9.5px;font-weight:600;color:var(--gold);line-height:11px;text-align:left}
.cover-year{position:absolute;right:10px;top:92px;font-size:45px;font-weight:700;color:var(--gold);line-height:1}
.cover-title{position:absolute;right:10px;top:140px;font-size:15.5px;font-weight:500;color:var(--brown);line-height:20.5px}

/* methodology */
.methodology{left:150px;top:11px;width:183px;height:208px;padding:15px 13px 0}
.methodology .heading{margin-bottom:10px}

/* trend chart */
.trend{left:343px;top:11px;width:535px;height:208px}
.trend .heading{position:absolute;left:13px;top:11px;color:var(--ink);font-weight:500}
.trend svg{position:absolute;left:0;top:0}
.trend-note{position:absolute;left:413px;top:10px;width:106px;height:189px;background:var(--olive);color:var(--white);padding:9px 8px;font-size:6.9px;line-height:10px;text-align:justify}

/* total */
.total{left:889px;top:11px;width:301px;height:208px}
.total-photo{position:absolute;left:10px;top:8px;width:150px;height:80px;border-radius:40px;background:radial-gradient(ellipse at 45% 50%,#eeeeee 0%,#d8d8d8 55%,rgba(249,162,28,0) 75%)}
.total-title{position:absolute;left:177px;top:12px;font-size:15px;font-weight:500;color:var(--brown)}
.total-sub{position:absolute;left:177px;top:29px;font-size:7px;color:var(--brown)}
.total-figure{position:absolute;right:11px;top:50px;font-size:58px;font-weight:700;color:var(--brown);line-height:1}
.total-copy{position:absolute;left:11px;top:111px;width:280px;font-size:6.6px;line-height:15.8px;color:var(--brown);text-align:justify}

/* bottom row */
.field-photo{left:11px;top:231px;width:128px;height:208px;background:linear-gradient(180deg,#7fa9d6 0%,#b9d1e6 45%,#9fbf63 70%,#4d7d1d 100%)}
.collection{left:150px;top:231px;width:203px;height:208px;padding:14px 14px 0 15px}
.collection .heading{margin-bottom:12px;line-height:16px}
.collection .copy{text-align:justify}

.figures{left:364px;top:231px;width:279px;height:208px}
.figure{position:absolute;top:16px;width:114px}
.figure--industrial{left:17px}
.figure--consumer{left:146px}
.figure-photo{width:114px;height:85px}
.figure-photo--industrial{background:linear-gradient(160deg,#e6e6e6,#a9acae 60%,#5e6062)}
.figure-photo--consumer{background:linear-gradient(160deg,#4a4a48,#8b8d86 50%,#d8d9d6)}
.figure-label{margin-top:16px;font-size:15px;font-weight:500;color:var(--ink);line-height:16px}
.figure-unit{font-size:6.8px;color:var(--ink)}
.figure-value{margin-top:2px;font-size:53px;font-weight:700;line-height:1;letter-spacing:-1px}
.figure--industrial .figure-value{color:var(--orange)}
.figure--consumer .figure-value{color:var(--olive)}

.split{left:654px;top:231px;width:535px;height:208px}
.split .heading{position:absolute;left:13px;top:11px;color:var(--ink);font-weight:500}
.split svg{position:absolute;left:0;top:0}
.split-note{position:absolute;left:390px;top:10px;width:130px;height:188px;background:var(--blue);color:var(--white);padding:9px 9px;font-size:7px;line-height:10px;text-align:justify}
</style>
</head>
<body>

<section class="panel panel--white cover">
  <div class="brand"><span class="brand-dot"></span><span class="brand-name">QRV Trade<br>Board</span></div>
  <div class="cover-year">2018</div>
  <h1 class="cover-title">EPS<br>RECYCLING<br>RATE REPORT</h1>
</section>

<section class="panel panel--blue methodology">
  <h2 class="heading">METHODOLOGY</h2>
  <div class="copy">
    <p>The 2017 Expanded Polystyrene Recycling Rate Study was conducted by the QRV-TB to gather data to reflect both post-consumer and post-industrial recycling activity. The 2017 results are based on data received from 55 EPS manufacturers and independent recyclers in the U.S.</p>
    <p>Participation in the EPS recycling survey is voluntary and the reported data is based on the responses received. Many companies have limited resources to put towards participation in the survey, and some companies may choose not to respond due to their confidentiality policies. Therefore, because there is not 100 percent participation, the presented totals represent the minimum amount of EPS recovered for recycling.</p>
  </div>
</section>

<section class="panel panel--white trend">
  <h2 class="heading">Post-Consumer EPS Recycling 1990-2018</h2>
  <svg width="535" height="208" viewBox="0 0 535 208" font-family="Raleway, sans-serif">
    <g stroke="var(--grid)" stroke-width=".7">
      <line x1="50" y1="48" x2="50" y2="192"/><line x1="73.6" y1="48" x2="73.6" y2="192"/>
      <line x1="97.3" y1="48" x2="97.3" y2="192"/><line x1="120.9" y1="48" x2="120.9" y2="192"/>
      <line x1="144.6" y1="48" x2="144.6" y2="192"/><line x1="168.2" y1="48" x2="168.2" y2="192"/>
      <line x1="191.8" y1="48" x2="191.8" y2="192"/><line x1="215.5" y1="48" x2="215.5" y2="192"/>
      <line x1="239.1" y1="48" x2="239.1" y2="192"/><line x1="262.8" y1="48" x2="262.8" y2="192"/>
      <line x1="286.4" y1="48" x2="286.4" y2="192"/><line x1="310" y1="48" x2="310" y2="192"/>
      <line x1="333.7" y1="48" x2="333.7" y2="192"/><line x1="357.3" y1="48" x2="357.3" y2="192"/>
      <line x1="381" y1="48" x2="381" y2="192"/>
    </g>
    <g font-size="5.5" fill="#666" text-anchor="end">
      <text x="37" y="189">0</text><text x="37" y="169">10</text><text x="37" y="149">20</text>
      <text x="37" y="129">30</text><text x="37" y="109">40</text><text x="37" y="89.5">50</text>
      <text x="37" y="69.5">60</text><text x="37" y="49.5">70</text>
    </g>
    <text x="0" y="0" font-size="5" fill="#888" transform="translate(22 160) rotate(-90)">Millions of Pounds Recycled</text>
    <g font-size="5.5" fill="#666" text-anchor="middle">
      <text x="50" y="194">1990</text><text x="73.6" y="194">1992</text><text x="97.3" y="194">1994</text>
      <text x="120.9" y="194">1996</text><text x="144.6" y="194">1998</text><text x="168.2" y="194">2000</text>
      <text x="191.8" y="194">2002</text><text x="215.5" y="194">2004</text><text x="239.1" y="194">2006</text>
      <text x="262.8" y="194">2008</text><text x="286.4" y="194">2010</text><text x="310" y="194">2012</text>
      <text x="333.7" y="194">2016</text><text x="357.3" y="194">2017</text><text x="381" y="194">2018</text>
    </g>
    <polyline fill="none" stroke="var(--olive)" stroke-width="1.5" points="50,181 73.6,145.7 97.3,138.9 120.9,142.3 144.6,150.9 168.2,137.5 191.8,135 215.5,137.3 239.1,123.4 262.8,120.3 286.4,113.3 310,114.1 333.7,61.9 357.3,135.6"/>
    <g font-size="5.5" fill="#444" text-anchor="middle">
      <text x="50" y="173">3.0</text><text x="73.6" y="139">20.8</text><text x="97.3" y="132">24.2</text>
      <text x="120.9" y="135.5">22.5</text><text x="144.6" y="144">18.2</text><text x="168.2" y="130.5">24.9</text>
      <text x="191.8" y="128">26.2</text><text x="215.5" y="130.5">25.0</text><text x="239.1" y="116.5">32.0</text>
      <text x="262.8" y="113.5">33.6</text><text x="286.4" y="106.5">37.1</text><text x="310" y="107.5">36.7</text>
      <text x="333.7" y="55">63.0</text><text x="357.3" y="143.5">25.9</text>
    </g>
  </svg>
  <p class="trend-note">The 25-year baseline shows incremental gains with more than 23 million pounds of EPS recycled annually on average. Like all commodity markets, the EPS recycling market is cyclical. The 2017 results reflect a decrease from 2016 due to the new landscape for recycling commodities and chaning international markets, especially in China.</p>
</section>

<section class="panel panel--orange total">
  <div class="total-photo" role="img" aria-label="Photo of a recycled foam block embossed with a recycling mark"></div>
  <h2 class="total-title">2018 Total</h2>
  <p class="total-sub">million pounds of EPS recycled</p>
  <div class="total-figure">65.0</div>
  <p class="total-copy">More than 65 million pounds of EPS were recycled during calendar year 2017. This figure includes 25.9 million pounds of post-consumer packaging and 39.0 million pounds of post-industrial recovery. Post-consumer is defined as any material that is recycled after its intended end-use while post-industrial recovery includes EPS facility scrap that is recycled but never served its intended purpose as a packaging material or other end-use application.</p>
</section>

<div class="panel field-photo" role="img" aria-label="Photo of green grass under a blue sky"></div>

<section class="panel panel--olive collection">
  <h2 class="heading">COLLECTION OPTIONS<br>&amp; RESOURCES</h2>
  <div class="copy">
    <p>Not everything can be recycled all the time. In order for materials to be recycled, stable markets must exist and there must be a demand for the end products. Each community has its own guidelines for which plastics are accepted, and these can vary widely. Some locations also offer consumer drop-off access. To find out if EPS recycling is available in your area, visit www.qrvtradeboard.org</p>
    <p>For consumers that do not have access to a local drop-off center, the QRV-TB sponsors a National Mail-Back Program intended for smaller quantities of EPS which can be mailed via NatPost or ParcelLine to more than 20 locations nationwide. Full instructions and a list of Mail-Back locations are available on the QRV-TB website.</p>
  </div>
</section>

<section class="panel panel--white figures">
  <div class="figure figure--industrial">
    <div class="figure-photo figure-photo--industrial" role="img" aria-label="Photo of stacked white foam scrap at a recycling facility"></div>
    <h3 class="figure-label">Post-Industrial</h3>
    <p class="figure-unit">(millions of pounds)</p>
    <div class="figure-value">39.0</div>
  </div>
  <div class="figure figure--consumer">
    <div class="figure-photo figure-photo--consumer" role="img" aria-label="Photo of a worker feeding a foam sheet into a recycling machine"></div>
    <h3 class="figure-label">Post-Consumer</h3>
    <p class="figure-unit">(millions of pounds)</p>
    <div class="figure-value">25.0</div>
  </div>
</section>

<section class="panel panel--white split">
  <h2 class="heading">EPS Recycling Post-Consumer &amp; Post-Industrial</h2>
  <svg width="535" height="208" viewBox="0 0 535 208" font-family="Raleway, sans-serif">
    <text x="13" y="50" font-size="5.5" fill="#444">(millions of pounds)</text>
    <rect x="15" y="61" width="6" height="6" fill="var(--olive)"/>
    <text x="26" y="66.5" font-size="5.5" fill="#444">POST-CONSUMER</text>
    <rect x="15" y="75" width="6" height="6" fill="var(--orange)"/>
    <text x="26" y="80.5" font-size="5.5" fill="#444">POST-INDUSTRIAL</text>
    <g fill="var(--olive)">
      <rect x="16" y="137.2" width="19" height="49.8"/>
      <rect x="68.9" y="137" width="19" height="50"/>
      <rect x="121.8" y="119.8" width="19" height="67.2"/>
      <rect x="174.7" y="113.6" width="19" height="73.4"/>
      <rect x="227.6" y="61" width="19" height="126"/>
      <rect x="280.5" y="135.2" width="19" height="51.8"/>
      <rect x="333.4" y="135.2" width="19" height="51.8"/>
    </g>
    <g fill="var(--orange)">
      <rect x="36" y="155.8" width="19" height="31.2"/>
      <rect x="88.9" y="121.2" width="19" height="65.8"/>
      <rect x="141.8" y="115.4" width="19" height="71.6"/>
      <rect x="194.7" y="73.2" width="19" height="113.8"/>
      <rect x="247.6" y="75.6" width="19" height="111.4"/>
      <rect x="300.5" y="109" width="19" height="78"/>
      <rect x="353.4" y="109" width="19" height="78"/>
    </g>
    <line x1="12" y1="187" x2="380" y2="187" stroke="#999" stroke-width=".6"/>
    <g font-size="5" text-anchor="middle" fill="var(--olive)">
      <text x="25.5" y="134">24.9</text><text x="78.4" y="134">25.0</text><text x="131.3" y="117">33.6</text>
      <text x="184.2" y="110.5">36.7</text><text x="237.1" y="58">63.0</text><text x="290" y="132">25.9</text>
      <text x="342.9" y="132">25.9</text>
    </g>
    <g font-size="5" text-anchor="middle" fill="var(--orange)">
      <text x="45.5" y="152.5">15.6</text><text x="98.4" y="118">32.9</text><text x="151.3" y="112">35.8</text>
      <text x="204.2" y="70">56.9</text><text x="257.1" y="72.5">55.7</text><text x="310" y="106">39.0</text>
      <text x="362.9" y="106">39.0</text>
    </g>
    <g font-size="5.5" text-anchor="middle" fill="#444">
      <text x="35.5" y="194">2000</text><text x="88.4" y="194">2004</text><text x="141.3" y="194">2008</text>
      <text x="194.2" y="194">2012</text><text x="247.1" y="194">2016</text><text x="300" y="194">2017</text>
      <text x="352.9" y="194">2018</text>
    </g>
  </svg>
  <p class="split-note">Despite lower collection amounts reflected in 2017, EPS has historically enjoyed consistent growth since its inception in the early 1990's. This decrease is a direct result of export restrictions on recycled plastics and a reprocessing plant closure that previously recycled large quantities of EPS. Newer EPS recycling technologies to facilitate EPS collection and reprocessing launched in 2018 indicate growth rates will continue on an upward trend in the future.</p>
</section>

</body>
</html>
```